"Pause. Pivot. Prosper." Empowerment Book Cover

Hello, I need a hot, trendy, and contemporary book cover designed for my first book called "Pause. Pivot. Prosper. -- 365 Bold Confidence Notes for Anyone Seeking to Pause, Pivot, and Prosper Across Career & Personal Dreams."
This is my first book and I am really wanting to launch my brand with it... it would be awesome to match the inside/outside branding of the book. So we can either create the book cover to match the book guts, or update the book guts to match the cover.
Lastly, I just got a professional photoshoot done last week so we can use one of those images, or we can go with a different idea/style for the cover. The body of the book is attached. All questions welcomed, happy designing!
Target Market(s)
Gen Z, Millennials and Gen X.
Industry/Entity Type
Personal Development.
Requirements
Must have
- It must stand out and be different from other typical book covers.
Nice to have
- Success, Inspiration, Motivation, Mindset, Growth.
Should not have
- Clipart, stock art, stock look and feel.

```html
<!DOCTYPE html>
<html lang="en">
<head>
<meta charset="utf-8">
<title>Pause. Pivot. Prosper. — Book Cover</title>
<link rel="stylesheet" href="https://fonts.googleapis.com/css2?family=Questrial&family=Nunito+Sans:wght@800&display=swap">
<style>
  :root {
    --page-grey: #e9e9e9;
    --cover-blue: #02a9de;
    --band-white: #ffffff;
  }
  * { margin: 0; padding: 0; box-sizing: border-box; }
  html, body {
    width: 851px;
    height: 1200px;
    overflow: hidden;
    background: var(--page-grey);
  }
  .canvas {
    position: relative;
    width: 851px;
    height: 1200px;
    background: var(--page-grey);
  }
  .cover {
    position: absolute;
    left: 72px;
    top: 74px;
    width: 706px;
    height: 1052px;
    background: var(--cover-blue);
  }
  .title-band {
    position: absolute;
    left: 0;
    height: 167px;
    background: var(--band-white);
    display: flex;
    align-items: center;
    padding-left: 14px;
    padding-right: 56px;
  }
  .title-band--one   { top: 111px; }
  .title-band--two   { top: 337px; }
  .title-band--three { top: 563px; width: 706px; }
  .title-word {
    font-family: "Questrial", "Century Gothic", sans-serif;
    font-size: 134px;
    line-height: 1;
    color: var(--cover-blue);
    letter-spacing: -1px;
    white-space: nowrap;
    padding-bottom: 6px;
  }
  .subtitle-band {
    position: absolute;
    left: 0;
    top: 818px;
    width: 706px;
    height: 76px;
    background: var(--band-white);
    display: flex;
    flex-direction: column;
    justify-content: center;
    align-items: center;
    gap: 3px;
  }
  .subtitle-line {
    font-family: "Nunito Sans", "Century Gothic", sans-serif;
    font-weight: 800;
    font-size: 15.5px;
    line-height: 1.15;
    color: var(--cover-blue);
    text-transform: uppercase;
    white-space: nowrap;
    letter-spacing: 0.2px;
  }
  .author {
    position: absolute;
    left: 0;
    top: 979px;
    width: 706px;
    text-align: center;
    font-family: "Questrial", "Century Gothic", sans-serif;
    font-size: 38px;
    line-height: 1;
    letter-spacing: 15px;
    padding-left: 15px;
    color: var(--band-white);
    text-transform: uppercase;
  }
</style>
</head>
<body>
  <main class="canvas">
    <section class="cover">
      <div class="title-band title-band--one"><h1 class="title-word">Pause.</h1></div>
      <div class="title-band title-band--two"><span class="title-word">Pivot.</span></div>
      <div class="title-band title-band--three"><span class="title-word">Prosper.</span></div>

      <div class="subtitle-band">
        <p class="subtitle-line">365 Bold Confidence Notes for Anyone Seeking to</p>
        <p class="subtitle-line">Pause, Pivot, and Prosper Across Career &amp; Personal Dreams</p>
      </div>

      <p class="author">Nadia Voss</p>
    </section>
  </main>
</body>
</html>
```